Forward thinking startup needs business cards

We are a new company entering the fall protection market and we need business cards. We provide equipment and supplies to a very large industry, and we aim to catch the attention of the end-user; not just the distributors. Please browse brovanteq.com for a better feel of our initial branding. The hog images are not required, but are here for inspiration. Also, they should not be prominent in the design as much as an accent. Many of our customers will be very high-end, so this should be considered as well.

Target Market(s)

Buyers for the safety industry. Some accounts will be very large, but most of these people are very down-to-earth.

Industry/Entity Type

Business

Contact Information for Business Card

Name and title
phone: 1-800-563-2814
fax: 740-318-5096
web: www.brovanteq.com
address: 712 Quarrybend Lane, Ashgrove, OH 43921 USA
room for cell number, direct office phone number, extension, and email

Font styles to use
Serif
Sans Serif

Colors
f37122
ffffff

Requirements
Must have
• Should be very clean and easy to read. We typically use orange and grey in our color schemes - #ef7c2d and #424242
Nice to have
• It would be nice to have room somewhere to incorporate some of the other logos from our family of companies. At the same time, it should not look weird if they aren't included.

```html
<!DOCTYPE html>
<html lang="en">
<head>
<meta charset="utf-8">
<title>Brovanteq Business Card</title>
<link href="https://fonts.googleapis.com/css2?family=Lato:wght@400;700;900&display=swap" rel="stylesheet">
<style>
  :root {
    --orange: #ef7c2d;
    --orange-deep: #e5701f;
    --grey: #424242;
    --grey-soft: #6a6a6a;
    --white: #ffffff;
    --paper: #f7f7f7;
    --backdrop: #2b2b2b;
  }
  * { margin: 0; padding: 0; box-sizing: border-box; }
  html, body {
    width: 1200px;
    height: 873px;
    overflow: hidden;
    background: var(--backdrop);
    font-family: "Lato", Arial, sans-serif;
  }
  .stage {
    width: 1200px;
    height: 873px;
    display: flex;
    align-items: center;
    justify-content: center;
    gap: 40px;
  }
  .card {
    position: relative;
    width: 520px;
    height: 300px;
    border-radius: 22px;
    overflow: hidden;
  }
  .card--back {
    background: linear-gradient(160deg, #f2873c 0%, var(--orange) 55%, var(--orange-deep) 100%);
  }
  .card--front {
    background: linear-gradient(160deg, var(--white) 0%, var(--paper) 100%);
  }

  .brand { position: absolute; text-align: left; }
  .brand__name {
    font-weight: 900;
    letter-spacing: 1px;
    text-transform: uppercase;
    line-height: 1;
  }
  .brand__tagline {
    font-weight: 900;
    line-height: 1;
    margin-top: 4px;
  }

  .card--back .brand { right: 44px; top: 150px; }
  .card--back .brand__name { font-size: 36px; color: var(--white); }
  .card--back .brand__tagline { font-size: 17px; color: var(--grey); }

  .card--front .brand { left: 138px; top: 34px; }
  .card--front .brand__name { font-size: 40px; color: var(--grey); }
  .card--front .brand__tagline { font-size: 19px; color: var(--grey); }

  .person {
    position: absolute;
    right: 40px;
    top: 104px;
    text-align: right;
  }
  .person__name {
    font-size: 21px;
    font-weight: 900;
    color: var(--orange);
    line-height: 1.1;
  }
  .person__title {
    font-size: 11px;
    font-weight: 400;
    letter-spacing: 0.5px;
    color: var(--grey-soft);
    text-transform: uppercase;
  }

  .address {
    position: absolute;
    left: 40px;
    top: 156px;
    font-size: 13.5px;
    font-weight: 900;
    color: var(--orange);
    white-space: nowrap;
  }
  .contacts {
    position: absolute;
    left: 40px;
    top: 194px;
    list-style: none;
  }
  .contacts li {
    display: flex;
    align-items: center;
    gap: 10px;
    font-size: 14.5px;
    font-weight: 700;
    color: var(--grey);
    height: 28px;
  }
  .contacts svg { width: 16px; height: 16px; fill: var(--orange); flex: none; }
</style>
</head>
<body>
<main class="stage">
  <section class="card card--back" aria-label="Card back">
    <div class="brand">
      <div class="brand__name">Brovanteq</div>
      <div class="brand__tagline">Built For The Climb</div>
    </div>
  </section>

  <section class="card card--front" aria-label="Card front">
    <div class="brand">
      <div class="brand__name">Brovanteq</div>
      <div class="brand__tagline">Built For The Climb</div>
    </div>

    <div class="person">
      <div class="person__name">Dana Whitcombe</div>
      <div class="person__title">Director</div>
    </div>

    <p class="address">712 Quarrybend Lane, Ashgrove, OH 43921 USA</p>

    <ul class="contacts">
      <li>
        <svg viewBox="0 0 16 16" aria-hidden="true"><path d="M3.6 1.5l2.2 2.6-1.2 1.6c.9 2 2.5 3.6 4.5 4.5l1.6-1.2 2.6 2.2-1.3 2.3C7 13.2 2.8 9 2.3 3z"/></svg>
        1-800-563-2814
      </li>
      <li>
        <svg viewBox="0 0 16 16" aria-hidden="true"><path d="M4 1h8v4H4zM1.5 6h13v6H12v3H4v-3H1.5zM5 10v4h6v-4z"/></svg>
        740-318-5096
      </li>
      <li>
        <svg viewBox="0 0 16 16" aria-hidden="true"><path d="M1 3h14v10H1zM2.5 4.5v.6L8 9l5.5-3.9v-.6z"/></svg>
        office@brovanteq.com
      </li>
    </ul>
  </section>
</main>
</body>
</html>
```